Rotomould Brochure

We need a conference brochure designed with a copy ready for print and also a PDF copy for email usage. We have mocked up something in word with the wording, the specific ads and images are provided in the file crate folder.

https://www.filecrate.net/sh/qk4tr82mxp51c07/HvLnQbsWERk?n=57104362

Reason: I have extended the deadline and offered more money as we understand the work is required.

```html
<!DOCTYPE html>
<html lang="en">
<head>
<meta charset="utf-8">
<title>Destination Sydney – Conference Brochure Spread</title>
<link href="https://fonts.googleapis.com/css2?family=Bree+Serif&family=Raleway:wght@200;400;700&display=swap" rel="stylesheet">
<style>
  :root {
    --canvas: #ffffff;
    --page-white: #ffffff;
    --orange: #f39220;
    --orange-light: #f6a445;
    --sky-top: #2b95d6;
    --sky-bottom: #3aa9e6;
    --navy: #1d3566;
    --ink: #3a3a3a;
    --white: #ffffff;
    --photo-sky: #5d9ee0;
    --photo-sand: #d9c9ae;
    --widget-dark: #1f2a4a;
    --coin-gold: #d9b24a;
    --site-blue: #5fb9ea;
  }
  * { margin: 0; padding: 0; box-sizing: border-box; }
  html, body { width: 1200px; height: 1000px; overflow: hidden; background: var(--canvas); }
  .canvas { position: relative; width: 1200px; height: 1000px; }

  .page { position: absolute; top: 100px; height: 775px; box-shadow: 2px 3px 6px rgba(0,0,0,.35); overflow: hidden; }

  /* Left page */
  .page--destination { left: 44px; width: 544px; background: var(--page-white); }
  .travel-notes {
    position: absolute; left: 30px; top: 30px; width: 86px;
    font: 400 8.3px/15px "Raleway", sans-serif; color: var(--ink);
    letter-spacing: -0.1px; hyphens: auto; -webkit-hyphens: auto;
  }
  .travel-notes p + p { margin-top: 15px; }
  .beach-photo {
    position: absolute; left: 137px; top: 0; width: 407px; height: 470px;
    background: linear-gradient(180deg, var(--photo-sky) 0%, #a9cdef 35%, #b8c9a0 52%, var(--photo-sand) 68%, #c4c0b8 100%);
  }
  .feature-panel {
    position: absolute; left: 137px; top: 410px; width: 407px; height: 365px;
    background: linear-gradient(180deg, rgba(243,146,32,0) 0%, var(--orange-light) 18%, var(--orange) 32%, var(--orange) 100%);
  }
  .feature-title { position: absolute; left: 26px; top: 18px; right: 33px; height: 90px; color: var(--white); font-weight: 400; }
  .feature-title__lead { position: absolute; left: 0; top: 0; font: 200 40px/1 "Raleway", sans-serif; letter-spacing: .5px; }
  .feature-title__city { position: absolute; right: 0; top: 36px; font: 400 52px/1 "Bree Serif", serif; letter-spacing: 2px; white-space: nowrap; }
  .feature-copy {
    position: absolute; left: 26px; top: 111px; width: 366px;
    column-count: 2; column-gap: 12px;
    font: 400 10.3px/13.6px "Raleway", sans-serif; color: var(--ink);
  }
  .feature-copy p + p { margin-top: 13.6px; }
  .feature-copy strong { font-family: "Bree Serif", serif; font-weight: 400; color: var(--navy); }

  /* Right page */
  .page--essentials { left: 617px; width: 548px; background: linear-gradient(180deg, var(--sky-top), var(--sky-bottom)); }
  .weather-widget {
    position: absolute; left: 40px; top: 58px; width: 303px; height: 149px;
    background: linear-gradient(180deg, #3a3a3a 0%, var(--widget-dark) 20%, #2a3d6e 100%);
    box-shadow: 3px 4px 6px rgba(0,0,0,.35);
  }
  .coin {
    position: absolute; left: 65px; top: 280px; width: 198px; height: 198px; border-radius: 50%;
    background: radial-gradient(circle at 40% 35%, #f3d77c, var(--coin-gold) 60%, #a47e22);
    box-shadow: 3px 4px 6px rgba(0,0,0,.35);
  }
  .site-preview {
    position: absolute; left: 211px; top: 573px; width: 305px; height: 147px;
    background: linear-gradient(180deg, #1d4f86 0%, #1d4f86 22%, var(--site-blue) 40%, #eaf4fb 100%);
    box-shadow: 3px 4px 6px rgba(0,0,0,.35);
  }
  .info-block { position: absolute; }
  .info-block h2 { font: 400 19px/22px "Bree Serif", serif; }
  .info-block p { margin-top: 6px; font: 400 10.2px/12.4px "Raleway", sans-serif; color: var(--navy); }
  .info-block--weather { left: 364px; top: 53px; width: 144px; }
  .info-block--weather h2 { color: var(--white); }
  .info-block--currency { left: 315px; top: 353px; width: 128px; }
  .info-block--currency h2 { color: var(--navy); }
  .info-block--visa { left: 37px; top: 568px; width: 124px; }
  .info-block--visa h2 { color: var(--white); white-space: nowrap; }
</style>
</head>
<body>
<div class="canvas">

  <section class="page page--destination">
    <aside class="travel-notes">
      <p>Flight Information NORTA recommends that you book your flights early and there are some great deals around at the moment. Domestic and International flights are directly into Sydney Airport. For departures we would recommend booking your flight out of Sydney after 3:00pm on Tuesday the 24th June.</p>
      <p>Hotel Transfers There are several options for getting to the hotel from the airport. The easiest is in a taxi and this will cost you approximately AUD$20 – AUD$30 each way. If you need assistance please contact NORTA.</p>
      <p>Travel Insurance NORTA Strongly recommends that all attendees have travel insurance. Anything can happen while overseas from injuring yourself to covering your conference costs if you are unable to attend at the last minute. If you need assistance with this please contact NORTA.</p>
    </aside>

    <div class="beach-photo" role="img" aria-label="Photo of a curved beachfront promenade with stepped seating, sand and apartment towers under a blue sky"></div>

    <div class="feature-panel">
      <h1 class="feature-title">
        <span class="feature-title__lead">Destination</span>
        <span class="feature-title__city">SYDNEY</span>
      </h1>
      <div class="feature-copy">
        <p><strong>Sydney</strong> is the most populous city in Australia and is built around the attractions of a working harbor, Sydney provides the largest and most dynamic economy in the country, with a highly skilled, multi-lingual workforce and quality lifestyle. High-rise buildings of the central business district look across the water at green headlands of national parks and comfortable garden suburbs. To the west, the World Heritage Blue Mountains stand as a spectacular barrier to the inland, while the ever-changing moods of the Pacific Ocean dominate the beaches, which stretch for miles north and south from the forbidding cliffs of Sydney Heads. Sydney’s cultural scene is vibrant.</p>
        <p>Coogee is a trendy beachside suburb in Sydney’s Eastern Suburbs, close to the city, airport and a buzzing strip of cafés, restaurants and shops. Stunning and sophisticated but free of pretention, Coogee locals embrace a laid-back, relaxed lifestyle. The jewel of Coogee is its spectacular beach, widely renowned as one of the most beautiful on the east coast of Australia.</p>
      </div>
    </div>
  </section>

  <section class="page page--essentials">
    <div class="weather-widget" role="img" aria-label="Weather app panel showing a sun icon, Local Weather Sydney hourly, 9°C"></div>
    <div class="info-block info-block--weather">
      <h2>Weather</h2>
      <p>It will be quite cold in Sydney at the time of our conference so we advise packing warmer clothes as well as a heavy coat/jacket for the evenings. With the sun out during the day it can be slightly warmer but with temperatures as low as 9°C be it is best to be prepared for the cold.</p>
    </div>

    <div class="coin" role="img" aria-label="Gold Australian one dollar coin"></div>
    <div class="info-block info-block--currency">
      <h2>Currency</h2>
      <p>The currency is Australian Dollars and internationals will be able to exchange money at the hotel reception.</p>
    </div>

    <div class="info-block info-block--visa">
      <h2>Visa<br>Information</h2>
      <p>Please check online for the Visa requirements to enter Australia from your country. If you need a formal letter of invitation to obtain your visa please contact NORTA.</p>
    </div>
    <div class="site-preview" role="img" aria-label="Screenshot of a government visa website page titled Visit Australia"></div>
  </section>

</div>
</body>
</html>
```